Pactwise - Training I Consulting I Review - Related to Contracts/Agreements

We provide legal services, we need a plattform to book video online trainings or local trainings classes and appointments (with calendar feature to select date and see availability at screen), payment over internet, legal document creation over webpage, videos will be produces in the next 3 - 4 moths so this is a place holder item. Participants for the Online trainings shall have a login in area with secured password. Appointments for local trainings and Consulting. Consider Outline in file attached. I can send you also a video with more explanation regarding the purpose.

Target Market(s)

Startup/scale up Software companies that intent to have an international business and need help with their contracts, to sell their products. Sales persons.

Industry/Entity Type

Legal

Coding

Coded - Design and coding required

Number of Pages Required

5+ page

Font styles to use
Serif
Sans Serif

Colors
000000
eeeeee
f5f5f5
ffffff
f8fcfd
3277b5
ecf7fb
cadf82
86cfc6

Requirements
Must have
• See file pactwise attached with outline. Moreover see here first starting point: https://moritz-ebbing.sitebuildr-demo.net/mysite-1 . Main inspiration comes from www.advisoryhub-demo.net from the log in area, see the outline in the file attached with the screen shots. At the end I need someone who can draft the full webpage and maintain it for a yearly fee. It must be simple and well structured layout. Lean. 1st landing page shall not scroll, 2 landing page only a little to see the testimonials and foster of page. There should be a Progress Bar to indicate the booking/selection process. Calendar booking. Easy fast booking.
• I like the colour mix, the feeling and the easy structor of:
• https://www.artpitch-demo.net/design/6374387or
• https://www.artpitch-demo.net/design/6372391 or https://www.artpitch-demo.net/design/6374366
• https://www.agencyfind-demo.net/en/web-design/belgium-be
• https://www.artpitch-demo.net/design/5896857
• https://www.artpitch-demo.net/design/5902173
• https://www.artpitch-demo.net/design/17197349
• https://www.artpitch-demo.net/design/5464461
• https://www.artpitch-demo.net/design/7180908
Nice to have
• page for evaluation and interview, see outline attached in the file with screen shots. Document upload.
Should not have
• many pictures, long scroll down pages on the 1st and 2nd ladding pages, many colours and forms. No need for news letter, search field, no need for links to Chatterly and other social media (except workNet).

```html
<!DOCTYPE html>
<html lang="en">
<head>
<meta charset="utf-8">
<title>Pactwise — Training / Design / Review</title>
<link rel="stylesheet" href="https://fonts.googleapis.com/css2?family=Montserrat:wght@500;600;700&family=Open+Sans:wght@400;600;700;800&family=Oswald:wght@500&display=swap">
<style>
  :root {
    --red: #e81f25;
    --lime: #cadf82;
    --ink: #111111;
    --white: #ffffff;
    --body-grey: #444444;
    --card-1: #1f1f1f;
    --card-2: #171717;
    --card-3: #0d0d0d;
    --section-dark: #1c1c1c;
    --footer: #161616;
    --footer-base: #0f0f0f;
  }
  * { box-sizing: border-box; margin: 0; padding: 0; }
  html, body { width: 828px; height: 1200px; overflow: hidden; background: var(--ink); }
  body { position: relative; font-family: "Open Sans", Arial, sans-serif; color: var(--white); }

  /* Hero */
  .hero { position: absolute; left: 0; top: 0; width: 828px; height: 290px;
    background: radial-gradient(ellipse at 30% 40%, #5a5650 0%, #3b3a38 40%, #222 100%); }
  .hero-photo { position: absolute; inset: 0; }
  .brand { position: absolute; left: 176px; top: 14px; font-family: "Montserrat", sans-serif;
    font-weight: 500; font-size: 14px; letter-spacing: 1px; color: var(--white); }
  .nav { position: absolute; right: 172px; top: 13px; display: flex; align-items: center; gap: 16px; }
  .nav a { font-family: "Montserrat", sans-serif; font-weight: 600; font-size: 7.5px; letter-spacing: .4px;
    color: var(--white); text-decoration: none; }
  .nav .login { background: var(--red); width: 69px; height: 21px; display: flex; align-items: center;
    justify-content: center; font-weight: 700; font-size: 8px; margin-left: 6px; }
  .hero-title { position: absolute; left: 0; width: 828px; top: 116px; text-align: center;
    font-family: "Montserrat", sans-serif; font-weight: 700; font-size: 31px; letter-spacing: 1.5px; }
  .hero-sub { position: absolute; left: 0; width: 828px; top: 157px; text-align: center;
    font-family: "Montserrat", sans-serif; font-weight: 500; font-size: 13px; letter-spacing: .6px; word-spacing: 4px; }
  .enter { position: absolute; left: 374px; top: 192px; width: 81px; height: 24px; background: var(--red);
    font-weight: 700; font-size: 8px; display: flex; align-items: center; justify-content: center; letter-spacing: .3px; }

  /* Services */
  .services { position: absolute; left: 0; top: 290px; width: 828px; height: 291px; background: var(--section-dark); }
  .service { position: absolute; top: 0; width: 248px; height: 225px; text-align: center; }
  .service:nth-child(1) { left: 42px; background: var(--card-1); }
  .service:nth-child(2) { left: 290px; background: var(--card-2); }
  .service:nth-child(3) { left: 538px; background: var(--card-3); width: 249px; }
  .service-icon { width: 78px; height: 78px; margin: 24px auto 0; border-radius: 50%; background: #151515;
    display: flex; align-items: center; justify-content: center; }
  .service-icon span { width: 70px; height: 70px; border-radius: 50%; background: var(--lime); display: block; }
  .service h2 { font-family: "Oswald", sans-serif; font-weight: 500; font-size: 14px; letter-spacing: .8px; margin-top: 23px; }
  .service p { font-size: 6.3px; line-height: 12px; width: 190px; margin: 7px auto 0; color: #e6e6e6; }
  .service a { display: inline-block; margin-top: 3px; font-size: 7px; font-weight: 600; color: var(--red); }
  .videos-title { position: absolute; left: 0; width: 828px; top: 246px; text-align: center; color: var(--red);
    font-weight: 800; font-size: 20px; letter-spacing: .5px; }

  /* Video */
  .video { position: absolute; left: 0; top: 581px; width: 828px; height: 227px;
    background: linear-gradient(180deg, #3a3633 0%, #2c2a28 55%, #1f1d1c 100%); }
  .play { position: absolute; left: 402px; top: 100px; }
  .track { position: absolute; left: 8px; top: 201px; width: 808px; height: 2px; background: #555; }
  .track .loaded { position: absolute; left: 0; top: 0; width: 646px; height: 2px; background: #9a9a9a; }
  .track .done { position: absolute; left: 0; top: 0; width: 381px; height: 2px; background: var(--red); }
  .controls { position: absolute; left: 10px; top: 207px; display: flex; gap: 7px; align-items: center;
    font-size: 4.5px; color: #ddd; }
  .controls-right { position: absolute; right: 10px; top: 207px; display: flex; gap: 7px; }

  /* Contact band */
  .contact { position: absolute; left: 0; top: 808px; width: 828px; height: 46px; background: var(--red);
    display: flex; align-items: center; justify-content: center; gap: 24px;
    font-weight: 700; font-size: 10px; letter-spacing: .2px; }
  .contact-item { display: flex; align-items: center; gap: 14px; }

  /* Testimonial */
  .testimonial { position: absolute; left: 0; top: 854px; width: 828px; height: 223px; background: var(--white);
    text-align: center; color: var(--body-grey); }
  .testimonial h2 { color: var(--red); font-weight: 800; font-size: 19px; margin-top: 38px; letter-spacing: .3px; }
  .quote { margin-top: 4px; }
  .testimonial p { width: 380px; margin: 6px auto 0; font-size: 7.6px; line-height: 13px; }
  .stars { margin-top: 4px; color: #aaa; font-size: 7px; letter-spacing: .5px; }
  .reviewer { color: var(--red); font-weight: 600; font-size: 9.5px; margin-top: 2px; }
  .dots { display: flex; justify-content: center; gap: 3px; margin-top: 10px; }
  .dots i { width: 7px; height: 7px; border-radius: 50%; background: #1a1a1a; display: block; }
  .dots i.active { background: var(--red); }

  /* Footer */
  .footer { position: absolute; left: 0; top: 1077px; width: 828px; height: 88px; background: var(--footer); }
  .footer-links { position: absolute; left: 172px; top: 27px; display: grid;
    grid-template-columns: repeat(4, 120.5px); row-gap: 11px; list-style: none; }
  .footer-links li { font-size: 7px; color: #e8e8e8; }
  .footer-links li::before { content: "»"; margin-right: 6px; }
  .footer-base { position: absolute; left: 0; top: 1165px; width: 828px; height: 35px; background: var(--footer-base); }
  .footer-brand { position: absolute; left: 174px; top: 9px; font-family: "Montserrat", sans-serif;
    font-weight: 500; font-size: 13px; letter-spacing: 1px; }
  .copyright { position: absolute; right: 173px; top: 12px; font-size: 6.5px; color: #e8e8e8; }
</style>
</head>
<body>

<header class="hero">
  <div class="hero-photo" role="img" aria-label="Photo of hands reviewing a contract with a pen beside a calculator"></div>
  <div class="brand">Pactwise</div>
  <nav class="nav">
    <a href="#">REFER SOMEONE</a>
    <a href="#">SERVICES</a>
    <a href="#">PARTNER</a>
    <a href="#" class="login">LOGIN</a>
  </nav>
  <h1 class="hero-title">PACTWISE</h1>
  <div class="hero-sub">TRAINING / DESIGN / REVIEW</div>
  <div class="enter">ENTER</div>
</header>

<section class="services">
  <article class="service">
    <div class="service-icon"><span role="img" aria-label="Icon of a trainer presenting to a group"></span></div>
    <h2>CONTRACT TRAINING</h2>
    <p>Lorem Ipsum is simply dummy text of the printing and typesetting industry. Lorem Ipsum has been the industry's standard dummy text ever since the 1500s.</p>
    <a>BOOK</a>
  </article>
  <article class="service">
    <div class="service-icon"><span role="img" aria-label="Icon of two people consulting at a table"></span></div>
    <h2>CONTRACT CONSULTING</h2>
    <p>Lorem Ipsum is simply dummy text of the printing and typesetting industry. Lorem Ipsum has been the industry's standard dummy text ever since the 1500s.</p>
    <a>APPOINTMENT</a>
  </article>
  <article class="service">
    <div class="service-icon"><span role="img" aria-label="Icon of a monitor with a reviewer and star rating"></span></div>
    <h2>CONTRACT REVIEW</h2>
    <p>Lorem Ipsum is simply dummy text of the printing and typesetting industry. Lorem Ipsum has been the industry's standard dummy text ever since the 1500s</p>
    <a>REQUEST</a>
  </article>
  <h2 class="videos-title">VIDEOS</h2>
</section>

<section class="video" role="img" aria-label="Video still of a smiling team in an office meeting">
  <svg class="play" width="22" height="26" viewBox="0 0 22 26"><path d="M0 0 L22 13 L0 26 Z" fill="#fff"/></svg>
  <div class="track"><div class="loaded"></div><div class="done"></div></div>
  <div class="controls">
    <svg width="7" height="7" viewBox="0 0 7 7"><rect x="0.5" y="0" width="2" height="7" fill="#fff"/><rect x="4.5" y="0" width="2" height="7" fill="#fff"/></svg>
    <svg width="8" height="7" viewBox="0 0 8 7"><path d="M0 0 L5 3.5 L0 7 Z" fill="#fff"/><rect x="6" y="0" width="1.5" height="7" fill="#fff"/></svg>
    <svg width="8" height="7" viewBox="0 0 8 7"><path d="M0 2 H2 L5 0 V7 L2 5 H0 Z" fill="#fff"/><path d="M6 2 Q7.5 3.5 6 5" stroke="#fff" fill="none"/></svg>
    <span>0:35 / 2:25</span>
  </div>
  <div class="controls-right">
    <svg width="8" height="7" viewBox="0 0 8 7"><rect x="0" y="1" width="8" height="5" fill="#fff"/></svg>
    <svg width="8" height="8" viewBox="0 0 8 8"><circle cx="4" cy="4" r="2.8" fill="none" stroke="#fff" stroke-width="2"/></svg>
    <svg width="9" height="7" viewBox="0 0 9 7"><rect x="0.5" y="0.5" width="8" height="6" fill="none" stroke="#fff"/></svg>
    <svg width="8" height="8" viewBox="0 0 8 8" fill="none" stroke="#fff"><path d="M0.5 3V0.5H3M5 0.5H7.5V3M7.5 5V7.5H5M3 7.5H0.5V5"/></svg>
  </div>
</section>

<section class="contact">
  <div class="contact-item">
    <svg width="28" height="20" viewBox="0 0 28 20" fill="none" stroke="#fff" stroke-width="1.2"><rect x="0.6" y="0.6" width="26.8" height="18.8"/><path d="M0.6 0.6 L14 11 L27.4 0.6M0.6 19.4 L10.5 8.5M27.4 19.4 L17.5 8.5"/></svg>
    <span>EMAIL: INFO@PACTWISE.COM</span>
  </div>
  <div class="contact-item">
    <svg width="26" height="26" viewBox="0 0 26 26" fill="none" stroke="#fff" stroke-width="1.2"><path d="M6 1 L10 7 L7.5 10 Q10 16 16 18.5 L19 16 L25 20 L22 25 Q10 24 3 13 Q0 6 6 1 Z"/></svg>
    <span>PHONE NUMBER: (123) 555 0147</span>
  </div>
</section>

<section class="testimonial">
  <h2>TESTIMONIAL</h2>
  <svg class="quote" width="24" height="17" viewBox="0 0 24 17" fill="#e81f25"><circle cx="5.5" cy="5.5" r="5.5"/><path d="M11 5.5 Q11 14 3 17 L2 15.5 Q6 13 6 9 Z"/><circle cx="18.5" cy="5.5" r="5.5"/><path d="M24 5.5 Q24 14 16 17 L15 15.5 Q19 13 19 9 Z"/></svg>
  <p>Lorem Ipsum is simply dummy text of the printing and typesetting industry. Lorem Ipsum has been the industry's standard dummy text ever since the 1500s, when an unknown printer took a galley of type and scrambled it to make a type specimen book</p>
  <div class="stars">★★★★★</div>
  <div class="reviewer">MARA TELLEN</div>
  <div class="dots"><i></i><i class="active"></i><i></i></div>
</section>

<footer class="footer">
  <ul class="footer-links">
    <li>Evaluation</li><li>Students</li><li>Policies</li><li>Team</li>
    <li>Market Feedback</li><li>Templates</li><li>Tools</li><li>Contact</li>
  </ul>
</footer>
<div class="footer-base">
  <div class="footer-brand">Pactwise</div>
  <div class="copyright">©2018 Pactwise.com</div>
</div>

</body>
</html>
```